I need a flyer made , the flyer can be one page or two pages or three pages . I will be posting this on Instagram and social media platforms. I am a luxury home builder , I am looking to hire a construction project manager . Below are some examples and ideas what can be on the flyer

We’re looking for a construction project manager who’s passionate about building luxury homes at the highest standards
We’re hiring construction project manager
* Experience 5+ years in residential project management with a strong portfolio of completed homes.
* location : Bergen County NJ
* excellent leadership skills, leads teams with confidence and clarity
* communicates seamlessly with architects , engineers, designers and clients
*knows how to manage budgets and timelines without compromising quality
*solves problems with a positive solution first mindset
* pays attention to every detail because in luxury the small things are the big things

Apply now , link in bio or DM to connect.

My logo is attached, my web site www.pinecrestbuildworks.com
My style is modern but still warm and inviting. I like a clean classy look .
Updates

Please don’t add any images of chairs or people to the flyer , I do not want people on my flyer. Do not add standard images of offices and houses , we are luxury builders , we build homes over 2 million dollars. Keep a classy , simple modern look . High end .

You can add a white hard hat with my logo on it for a image , this is a suggestion does not have to be on my flyer ,

```html
<!DOCTYPE html>
<html lang="en">
<head>
<meta charset="utf-8">
<title>Pinecrest Buildworks – We're Hiring</title>
<link href="https://fonts.googleapis.com/css2?family=Poppins:wght@200;300;400;700&display=swap" rel="stylesheet">
<style>
  :root {
    --backdrop: #ccd1d8;
    --panel: #e8ebeb;
    --ink: #0d0d0d;
    --band-grey: #cfd4da;
    --rule-grey: #a9adb4;
    --bullet-grey: #9a9ea4;
    --white: #ffffff;
    --photo-deep: #2d4a5a;
    --photo-mid: #6f8fa0;
    --photo-warm: #b89a6a;
    --haze-1: #dfe3e3;
    --haze-2: #c9d0cf;
  }
  * { margin: 0; padding: 0; box-sizing: border-box; }
  html, body { width: 1200px; height: 655px; overflow: hidden; }
  body { background: var(--backdrop); font-family: "Poppins", sans-serif; color: var(--ink); position: relative; }

  .page {
    position: absolute; top: 85px; width: 489px; height: 489px;
    background: linear-gradient(160deg, var(--haze-1) 0%, var(--panel) 45%, var(--haze-2) 100%);
    box-shadow: 0 6px 16px rgba(40, 50, 60, 0.25);
    overflow: hidden;
  }
  .page--cover { left: 94px; }
  .page--details { left: 596px; }
  .page svg.art { position: absolute; inset: 0; width: 489px; height: 489px; }

  .brand { position: absolute; top: 42px; font-family: "Poppins", sans-serif; font-weight: 300; font-size: 21px; letter-spacing: 1px; line-height: 1.15; text-transform: uppercase; color: var(--ink); }
  .brand small { display: block; font-size: 21px; }
  .page--cover .brand { left: 19px; }
  .page--details .brand { right: 19px; text-align: right; }

  .cover-title { position: absolute; left: 128px; top: 100px; width: 260px; text-align: right; }
  .cover-title__light { display: block; font-weight: 200; font-size: 72px; line-height: 1; letter-spacing: -2px; margin-right: 32px; }
  .cover-title__bold { display: block; font-weight: 700; font-size: 70px; line-height: 1; letter-spacing: -2px; margin-top: 2px; }

  .footer-bar { position: absolute; left: 0; top: 0; }
  .site { position: absolute; top: 448px; font-weight: 300; font-size: 9px; color: var(--white); }
  .page--cover .site { left: 19px; }
  .page--details .site { right: 19px; }

  .intro { position: absolute; right: 19px; top: 105px; width: 260px; text-align: right; font-weight: 700; font-size: 12.6px; line-height: 14.6px; }

  .role { position: absolute; right: 19px; top: 200px; text-align: right; }
  .role__kicker { display: block; font-weight: 200; font-size: 28px; line-height: 30px; letter-spacing: -0.5px; }
  .role__title { display: block; font-weight: 700; font-size: 30px; line-height: 26px; letter-spacing: -0.3px; margin-top: 2px; }
  .role-rule { position: absolute; left: 208px; right: 19px; top: 288px; height: 3px; background: var(--rule-grey); }

  .requirements { position: absolute; left: 51px; top: 300px; list-style: none; }
  .requirements li { position: relative; padding-left: 10px; font-weight: 300; font-size: 8.6px; line-height: 18.2px; white-space: nowrap; }
  .requirements li::before { content: ""; position: absolute; left: 0; top: 7px; width: 4px; height: 4px; background: var(--bullet-grey); }

  .cta { position: absolute; left: 19px; top: 442px; font-size: 11px; line-height: 12px; text-transform: uppercase; }
  .cta strong { display: block; font-weight: 700; }
  .cta span { display: block; font-weight: 300; }
</style>
</head>
<body>

  <section class="page page--cover">
    <svg class="art" viewBox="0 0 489 489" aria-hidden="false">
      <defs>
        <linearGradient id="villaGlow" x1="0" y1="0" x2="1" y2="1">
          <stop offset="0" stop-color="#8a7a5e"/>
          <stop offset="0.45" stop-color="#4d6f82"/>
          <stop offset="0.7" stop-color="#2f8aa0"/>
          <stop offset="1" stop-color="#2c3a2c"/>
        </linearGradient>
        <linearGradient id="sketchHaze" x1="0" y1="0" x2="0" y2="1">
          <stop offset="0" stop-color="#dde1e1"/>
          <stop offset="1" stop-color="#d0d5d5"/>
        </linearGradient>
      </defs>
      <rect x="0" y="190" width="240" height="250" fill="url(#sketchHaze)" role="img" aria-label="Faint architectural line sketch of a modern multi-level house"/>
      <rect x="300" y="439" width="189" height="32" fill="var(--band-grey)"/>
      <polygon points="489,236 116,489 352,489 489,351" fill="url(#villaGlow)" role="img" aria-label="Photo of a hillside luxury villa at dusk with lit glass floors and an infinity pool"/>
      <polygon points="0,439 160,439 129,471 0,471" fill="var(--ink)"/>
    </svg>
    <div class="brand">Pinecrest<small>Buildworks</small></div>
    <h1 class="cover-title">
      <span class="cover-title__light">WE’RE</span>
      <span class="cover-title__bold">HIRING</span>
    </h1>
    <p class="site">www.pinecrestbuildworks.com</p>
  </section>

  <section class="page page--details">
    <svg class="art" viewBox="0 0 489 489">
      <defs>
        <linearGradient id="villaNight" x1="0" y1="0" x2="1" y2="1">
          <stop offset="0" stop-color="#2f4a32"/>
          <stop offset="0.5" stop-color="#6b6a60"/>
          <stop offset="0.75" stop-color="#a98c5c"/>
          <stop offset="1" stop-color="#4f6f84"/>
        </linearGradient>
      </defs>
      <polygon points="105,0 340,0 0,340 0,105" fill="url(#villaNight)" role="img" aria-label="Photo of a cantilevered luxury home with warm interior lighting among trees"/>
      <rect x="0" y="439" width="489" height="32" fill="var(--band-grey)"/>
      <polygon points="353,439 489,439 489,471 321,471" fill="var(--ink)"/>
    </svg>
    <div class="brand">Pinecrest<small>Buildworks</small></div>
    <p class="intro">We’re looking for a construction project manager who’s passionate about building luxury homes at the highest standards</p>
    <h2 class="role">
      <span class="role__kicker">WE’RE HIRING</span>
      <span class="role__title">CONSTRUCTION<br>PROJECT MANAGER</span>
    </h2>
    <div class="role-rule"></div>
    <ul class="requirements">
      <li>Experience 5+ years in residential project management with a strong portfolio of completed homes</li>
      <li>Location : Bergen County NJ</li>
      <li>Excellent leadership skills, leads teams with confidence and clarity</li>
      <li>Communicates seamlessly with architects, engineers, designers and clients</li>
      <li>Knows how to manage budgets and timelines without compromising quality</li>
      <li>Solves problems with a positive solution first mindset</li>
      <li>Pays attention to every detail because in luxury the small things are the big things</li>
    </ul>
    <p class="cta"><strong>Apply now,</strong><span>Link in bio or DM to connect</span></p>
    <p class="site">www.pinecrestbuildworks.com</p>
  </section>

</body>
</html>
```